TradeFolks
Join the Sales & Marketing Community
Professional
Marta Zinelli
Partner
Via Corsetti 8
20100 Milano
marta.zinelli@tradefolks-example.it
www.tradefolks-example.it
Use the same design and colors of our winner logo in project "logo"

```html
<!DOCTYPE html>
<html lang="en">
<head>
<meta charset="utf-8">
<title>TradeFolks Stationery</title>
<link href="https://fonts.googleapis.com/css2?family=Open+Sans:wght@400;700&display=swap" rel="stylesheet">
<style>
:root{
  --bg:#8a8a8c;
  --paper:#ffffff;
  --plum:#3f1752;
  --magenta:#c2185b;
  --orange:#f39a1e;
  --ink:#4a3a52;
  --faint:#f3eef2;
}
*{margin:0;padding:0;box-sizing:border-box}
html,body{width:1200px;height:338px;overflow:hidden;background:var(--bg);font-family:"Open Sans",Arial,sans-serif;color:var(--ink)}
.stage{position:relative;width:1200px;height:338px}
.piece{position:absolute;background:var(--paper);overflow:hidden;box-shadow:0 1px 3px rgba(0,0,0,.35)}
.band{position:absolute;left:0;right:0;background:linear-gradient(90deg,var(--plum),var(--magenta),var(--plum))}
.brand{position:absolute;display:flex;align-items:center;gap:3px;font-weight:700;color:var(--magenta);white-space:nowrap}
.brand .dot{border-radius:50%;background:var(--plum)}
.fine{position:absolute;font-size:3px;line-height:4.2px;color:var(--ink);white-space:nowrap}
.watermark{position:absolute;border-radius:50%;background:var(--faint)}

/* business cards */
.card-front{left:28px;top:96px;width:66px;height:38px}
.card-back{left:28px;top:141px;width:66px;height:38px}

/* letterheads */
.letterhead{top:19px;width:145px;height:300px}
.letterhead.first{left:110px}
.letterhead.second{left:325px}

/* envelopes front */
.envelope{left:497px;width:186px;height:90px}
.envelope.top{top:112px}
.envelope.bottom{top:214px}

/* envelope backs */
.env-back{position:absolute;left:700px;width:193px}
</style>
</head>
<body>
<div class="stage">

  <!-- business card front -->
  <div class="piece card-front">
    <div class="band" style="top:0;height:3px"></div>
    <div class="brand" style="left:5px;top:7px;font-size:6px"><span class="dot" style="width:5px;height:5px"></span>TradeFolks</div>
    <div class="fine" style="left:5px;top:20px">Marta Zinelli · Partner<br>Via Corsetti 8, 20100 Milano<br>marta.zinelli@tradefolks-example.it</div>
    <div class="band" style="bottom:0;height:3px"></div>
  </div>

  <!-- business card back -->
  <div class="piece card-back">
    <div class="brand" style="left:16px;top:14px;font-size:7px"><span class="dot" style="width:6px;height:6px"></span>TradeFolks</div>
    <div class="band" style="bottom:0;height:3px"></div>
  </div>

  <!-- letterhead first page -->
  <div class="piece letterhead first">
    <div class="band" style="top:0;height:4px"></div>
    <div class="brand" style="left:9px;top:10px;font-size:7px"><span class="dot" style="width:6px;height:6px"></span>TradeFolks</div>
    <div class="fine" style="left:78px;top:10px">Via Corsetti 8<br>20100 Milano<br>www.tradefolks-example.it</div>
    <div class="watermark" style="left:72px;top:195px;width:60px;height:60px"></div>
    <div class="fine" style="left:36px;top:286px">Join the Sales &amp; Marketing Community</div>
    <div class="band" style="bottom:0;height:4px"></div>
  </div>

  <!-- letterhead second page -->
  <div class="piece letterhead second">
    <div class="band" style="top:0;height:4px"></div>
    <div class="watermark" style="left:72px;top:195px;width:60px;height:60px"></div>
    <div class="fine" style="left:36px;top:286px">Join the Sales &amp; Marketing Community</div>
    <div class="band" style="bottom:0;height:4px"></div>
  </div>

  <!-- envelope fronts -->
  <div class="piece envelope top">
    <div class="band" style="top:0;height:4px"></div>
    <div class="brand" style="left:8px;top:10px;font-size:7px"><span class="dot" style="width:6px;height:6px"></span>TradeFolks</div>
    <div class="fine" style="left:8px;top:22px">Via Corsetti 8 · 20100 Milano</div>
    <div class="band" style="bottom:0;height:4px"></div>
  </div>
  <div class="piece envelope bottom">
    <div class="band" style="top:0;height:4px"></div>
    <div class="brand" style="left:8px;top:10px;font-size:7px"><span class="dot" style="width:6px;height:6px"></span>TradeFolks</div>
    <div class="fine" style="left:8px;top:22px">Via Corsetti 8 · 20100 Milano</div>
    <div class="band" style="bottom:0;height:4px"></div>
  </div>

  <!-- envelope backs -->
  <svg class="env-back" style="top:19px" width="193" height="200" viewBox="0 0 193 200">
    <defs>
      <radialGradient id="flapPlum" cx="50%" cy="40%" r="70%">
        <stop offset="0" stop-color="#c2185b"/>
        <stop offset="1" stop-color="#3f1752"/>
      </radialGradient>
      <linearGradient id="flapOrange" x1="0" y1="0" x2="1" y2="0">
        <stop offset="0" stop-color="#f6b03a"/>
        <stop offset="0.5" stop-color="#ef7d1e"/>
        <stop offset="1" stop-color="#f6b03a"/>
      </linearGradient>
    </defs>
    <!-- open flap envelope -->
    <path d="M0 42 L14 4 Q16 0 22 0 L171 0 Q177 0 179 4 L193 42 Z" fill="url(#flapPlum)"/>
    <rect x="0" y="42" width="193" height="52" fill="#ffffff"/>
    <path d="M0 42 L96 78 L193 42" fill="none" stroke="#e6e6e6" stroke-width="1"/>
    <!-- closed flap envelope -->
    <rect x="0" y="100" width="193" height="95" fill="#ffffff"/>
    <path d="M0 100 L193 100 L193 106 L100 152 Q96 154 92 152 L0 106 Z" fill="url(#flapOrange)"/>
    <path d="M0 195 L96 150 L193 195" fill="none" stroke="#e2e2e2" stroke-width="1"/>
    <circle cx="96" cy="170" r="3" fill="#3f1752"/>
  </svg>

</div>
</body>
</html>
```